Private Dining Restaurant Menu Design

Looking for help in designing a private dining room menu brochure - probably would need 4 panel layout to make all of the content fit, or a 5.5x8" booklet. Open to your ideas on layout/vessel - would want to post on website and be able to print to hand out to guests interested in booking our private dining room.

All content is in the attached "Private Dining Menu".

Would like to match existing dinner menu design - also attached.

Website is www.tallowfenkitchen.com

Requirements
Must have
• Easy to read format of a brochure of the private dining menu content - want to be able to hand out to interested guests and have it simple and easy to read/flip through.

```html
<!DOCTYPE html>
<html lang="en">
<head>
<meta charset="utf-8">
<title>Tallowfen Private Dining Brochure</title>
<link rel="stylesheet" href="https://fonts.googleapis.com/css2?family=Montserrat:wght@400;600;700&family=Open+Sans:wght@400;600;700&family=Great+Vibes&display=swap">
<style>
  :root{
    --navy:#1d2b4c;
    --navy-deep:#162240;
    --red:#a3282c;
    --paper:#f5f4f0;
    --ink:#2b2d38;
    --muted:#5b5e6b;
    --rule:#c9c6bd;
    --stage:#d8d8d8;
    --white:#ffffff;
  }
  *{box-sizing:border-box;margin:0;padding:0}
  html,body{width:1200px;height:3158px;overflow:hidden}
  body{background:var(--stage);font-family:"Open Sans",Arial,sans-serif;color:var(--ink)}
  .sheet{display:flex;flex-direction:column;gap:77px;padding:77px 30px}
  .spread{display:flex;width:1140px;height:950px;box-shadow:0 6px 18px rgba(0,0,0,.18)}
  .page{position:relative;width:570px;height:950px;background:var(--paper);overflow:hidden}
  .page + .page{border-left:1px solid #dcdad3}

  /* ---------- cover ---------- */
  .brand-name{font-family:"Montserrat",sans-serif;font-weight:700;letter-spacing:2px;text-align:center;color:var(--red)}
  .brand-tag{font-family:"Montserrat",sans-serif;font-weight:600;font-size:11px;letter-spacing:3px;text-align:center;color:var(--navy)}
  .front{padding:58px 34px 0}
  .front .brand-name{font-size:44px;line-height:1}
  .front .brand-tag{margin-top:8px}
  .red-rule{height:3px;background:var(--red);margin:22px 0 12px;position:relative}
  .red-rule::before,.red-rule::after{content:"";position:absolute;top:-3px;width:9px;height:9px;border-radius:50%;background:var(--red)}
  .red-rule::before{left:-4px}.red-rule::after{right:-4px}
  .photo-grid{position:relative;display:grid;grid-template-columns:62% 1fr;grid-template-rows:1fr 1fr;gap:6px;height:360px}
  .photo{border-radius:2px}
  .photo-burger{grid-row:1/3;background:radial-gradient(ellipse at 45% 35%,#d9a25e 0%,#8a3a22 45%,#4a1e14 100%)}
  .photo-rice{background:linear-gradient(135deg,#e3c27a,#b7822f 60%,#6e8a3a)}
  .photo-steak{background:linear-gradient(135deg,#c2452c,#8c5a2e 55%,#4f6e2c)}
  .badge{position:absolute;left:54%;top:38%;width:104px;height:104px;border-radius:50%;background:var(--white);border:3px solid var(--navy);transform:translate(-50%,-50%)}
  .thin-rule{height:1px;background:var(--navy);width:40%;margin:16px auto 0}
  .tagline-band{margin:18px -34px 0;background:var(--navy);border-top:3px solid var(--rule);border-bottom:3px solid var(--rule);text-align:center;padding:8px 0}
  .script{font-family:"Great Vibes",cursive}
  .tagline-band .script{color:var(--white);font-size:34px}
  .order-label{text-align:center;color:var(--navy);font-size:36px;margin-top:22px}
  .order-phone{text-align:center;font-family:"Montserrat",sans-serif;font-weight:700;font-size:58px;color:var(--navy);line-height:1.1}
  .order-web{display:flex;align-items:center;justify-content:center;gap:14px;margin-top:14px;font-family:"Montserrat",sans-serif;font-weight:600;font-size:22px;color:var(--red)}
  .order-web svg{width:90px;height:12px}

  .back{background:var(--navy);padding:28px}
  .back-frame{position:absolute;inset:26px;border:1.5px solid rgba(255,255,255,.7)}
  .back-frame::after{content:"";position:absolute;inset:6px;border:1px solid rgba(255,255,255,.35)}
  .back-inner{position:relative;height:100%;display:flex;flex-direction:column;align-items:center;padding-top:70px}
  .back .brand-tag{color:var(--white);font-size:17px;letter-spacing:5px}
  .back .brand-name{color:var(--white);font-size:40px;margin-top:150px}
  .back-rule{width:220px;height:1px;background:rgba(255,255,255,.6);margin:26px 0}
  .back-photos{display:flex;gap:10px;margin-top:10px}
  .back-photos .photo{width:140px;height:110px;border:2px solid var(--white)}
  .bp-1{background:linear-gradient(135deg,#e6c98c,#a86b34)}
  .bp-2{background:linear-gradient(135deg,#c8873e,#6e3a1c 60%,#5f7d2e)}
  .bp-3{background:linear-gradient(135deg,#e7b97a,#8a4a2a)}
  .back-web{margin-top:auto;margin-bottom:70px;color:rgba(255,255,255,.8);font-family:"Montserrat",sans-serif;font-size:18px;letter-spacing:1px;display:flex;align-items:center;gap:16px}
  .back-web span.line{width:70px;height:1px;background:rgba(255,255,255,.6)}

  /* ---------- inside pages ---------- */
  .inside{padding:48px 38px 30px}
  .inside::before{content:"";position:absolute;left:0;right:0;top:0;height:10px;background:var(--red)}
  .inside::after{content:"";position:absolute;left:0;right:0;top:10px;height:3px;background:var(--navy)}
  .sec-title{font-family:"Montserrat",sans-serif;font-weight:700;font-size:13.5px;color:var(--navy);letter-spacing:.5px;margin:14px 0 5px;display:flex;align-items:center;gap:8px}
  .sec-title::before{content:"";width:0;height:0;border-left:7px solid var(--red);border-top:5px solid transparent;border-bottom:5px solid transparent}
  .body-text{font-size:11.5px;line-height:1.55;color:var(--muted)}
  .body-text strong{color:var(--ink)}
  .list{list-style:none;font-size:11.5px;line-height:1.6;color:var(--muted);padding-left:16px}
  .list li::before{content:"• ";color:var(--red);font-weight:700}
  .page-head{display:flex;align-items:center;gap:14px;justify-content:center;font-family:"Montserrat",sans-serif;font-weight:700;font-size:22px;letter-spacing:3px;color:var(--navy);margin-bottom:8px}
  .page-head::before,.page-head::after{content:"";flex:1;height:1px;background:var(--navy)}
  .head-note{font-size:11px;font-style:italic;text-align:center;color:var(--muted);margin-bottom:8px}
  .menu-row{display:flex;font-size:11.5px;line-height:1.7;color:var(--muted);padding-left:16px}
  .menu-row .dots{flex:1;border-bottom:1px dotted var(--rule);margin:0 6px 5px}
  .menu-row .price{color:var(--ink);font-weight:600}
  .photo-strip{display:flex;gap:10px;position:absolute;left:38px;right:38px;bottom:34px}
  .photo-strip .photo{flex:1;height:130px}
  .ms-1{background:linear-gradient(135deg,#d6b36a,#6e8a3a 60%,#b7452c)}
  .ms-2{background:linear-gradient(135deg,#b9bcc4,#6d6050)}
  .ms-3{background:linear-gradient(135deg,#c8413a,#e2c58e 60%,#8c2c2a)}

  .option-title{font-family:"Montserrat",sans-serif;font-weight:700;font-size:15px;color:var(--navy);margin:14px 0 4px}
  .lunch-photos{position:absolute;left:0;right:0;bottom:0;height:390px}
  .interior{position:absolute;left:0;top:40px;width:300px;height:350px;background:linear-gradient(160deg,#8b8e95,#3e3a36 55%,#6a4b32)}
  .food-stack{position:absolute;left:262px;top:0;display:flex;flex-direction:column;gap:10px}
  .food-item{display:flex;align-items:center;gap:14px}
  .food-item .photo{width:120px;height:100px;border:3px solid var(--white);box-shadow:0 2px 6px rgba(0,0,0,.2)}
  .food-caption{font-size:12px;font-weight:600;color:var(--navy);line-height:1.3;width:130px}
  .lp-1{background:linear-gradient(135deg,#7fa24a,#d9c07a 60%,#c0502c)}
  .lp-2{background:linear-gradient(135deg,#e8c26c,#a25a2a)}
  .lp-3{background:linear-gradient(135deg,#c42f3a,#e9d0a4 55%,#6a9a3c)}
  .dining-photo{float:left;width:200px;height:150px;margin:6px 16px 6px 0;background:linear-gradient(160deg,#a9a59d,#4a423a 60%,#7c6a55)}
  .dinner-photo{position:absolute;left:0;right:0;bottom:0;height:300px;background:radial-gradient(ellipse at 55% 60%,#a6552a 0%,#5b2a18 45%,#2f3a22 80%,#f5f4f0 100%)}
</style>
</head>
<body>
<main class="sheet">

  <!-- Outer spread: back cover + front cover -->
  <section class="spread outer-spread">
    <article class="page back">
      <div class="back-frame"></div>
      <div class="back-inner">
        <p class="brand-tag">WOOD-FIRED GRILL AND BAR</p>
        <p class="brand-name">TALLOWFEN</p>
        <div class="back-rule"></div>
        <div class="back-photos">
          <div class="photo bp-1" role="img" aria-label="Photo of a plated sandwich and fries"></div>
          <div class="photo bp-2" role="img" aria-label="Photo of a grilled burger"></div>
          <div class="photo bp-3" role="img" aria-label="Photo of a stack of pancakes"></div>
        </div>
        <div class="back-rule"></div>
        <p class="back-web"><span class="line"></span>tallowfenkitchen.com<span class="line"></span></p>
      </div>
    </article>

    <article class="page front">
      <p class="brand-name">TALLOWFEN</p>
      <p class="brand-tag">WOOD-FIRED GRILL AND BAR</p>
      <div class="red-rule"></div>
      <div class="photo-grid">
        <div class="photo photo-burger" role="img" aria-label="Photo of a pulled pork sandwich"></div>
        <div class="photo photo-rice" role="img" aria-label="Photo of seasoned rice with vegetables"></div>
        <div class="photo photo-steak" role="img" aria-label="Photo of grilled chicken with salad"></div>
        <div class="badge"></div>
      </div>
      <div class="red-rule"></div>
      <div class="thin-rule"></div>
      <div class="tagline-band"><p class="script">Fresh Food Made From Scratch</p></div>
      <p class="order-label script">Delivery Order</p>
      <p class="order-phone">04 55501872</p>
      <p class="order-web">
        <svg viewBox="0 0 90 12"><line x1="0" y1="6" x2="84" y2="6" stroke="#1d2b4c" stroke-width="1.5"/><path d="M84 1 L90 6 L84 11 Z" fill="#1d2b4c"/></svg>
        tallowfenkitchen.com
        <svg viewBox="0 0 90 12"><line x1="6" y1="6" x2="90" y2="6" stroke="#1d2b4c" stroke-width="1.5"/><path d="M6 1 L0 6 L6 11 Z" fill="#1d2b4c"/></svg>
      </p>
    </article>
  </section>

  <!-- Inside spread 1: room details + menu -->
  <section class="spread">
    <article class="page inside">
      <h2 class="sec-title">PRIVATE DINING ROOM</h2>
      <p class="body-text">Thank you for your interest in our private dining room. Our room is perfect for birthdays, rehearsal dinners, business lunches and family gatherings. Our team will help you plan every detail so you can relax and enjoy your guests.</p>
      <h2 class="sec-title">FOOD AND BEVERAGE ROOM MINIMUM (BEFORE TAX/GRATUITY)</h2>
      <ul class="list">
        <li>Sunday – Thursday, lunch: $150 &nbsp;·&nbsp; dinner: $300</li>
        <li>Friday – Saturday, lunch: $250 &nbsp;·&nbsp; dinner: $500</li>
      </ul>
      <p class="body-text" style="margin-top:6px"><strong>Gratuity:</strong> An automatic 18% gratuity will be added to the bill for all private dining room events.</p>
      <h2 class="sec-title">ROOM CAPACITY/LAYOUT OPTIONS:</h2>
      <ul class="list">
        <li>Long table seating: up to 24 guests</li>
        <li>Round tables: up to 32 guests seated</li>
        <li>Cocktail style: up to 45 guests standing</li>
        <li>Classroom or theater style on request</li>
      </ul>
      <p class="body-text" style="margin-top:6px">Please choose your layout when booking. The room may be reserved for up to four hours; extra time can be added for a small fee.</p>
      <h2 class="sec-title">MISCELLANEOUS SERVICES:</h2>
      <ul class="list">
        <li><strong>Linen Fee:</strong> white linens are available for $25 total</li>
        <li><strong>Cake Cutting Fee:</strong> $1 per guest for outside cakes</li>
        <li><strong>Corkage Fee:</strong> $15 per bottle brought in by guests</li>
        <li><strong>Audio Visual:</strong> screen, projector and microphone free</li>
        <li><strong>Decorations:</strong> welcome, but no confetti or glitter</li>
      </ul>
      <p class="body-text" style="margin-top:10px">A deposit is required to hold your date. Final guest count and menu choices are due one week before your event. Please contact our events team with any questions; we look forward to hosting you.</p>
    </article>

    <article class="page inside">
      <h2 class="page-head">MENU</h2>
      <h3 class="sec-title">APPETIZERS <span style="font-weight:400;font-size:11px">(price is by the dozen)</span></h3>
      <div class="menu-row"><span>Buffalo Chicken Wings</span><span class="dots"></span><span class="price">$15</span></div>
      <div class="menu-row"><span>Smoked Pork Sliders</span><span class="dots"></span><span class="price">$18</span></div>
      <div class="menu-row"><span>Spinach &amp; Artichoke Dip Bites</span><span class="dots"></span><span class="price">$14</span></div>
      <div class="menu-row"><span>Mini Crab Cakes</span><span class="dots"></span><span class="price">$24</span></div>
      <h3 class="sec-title">PLATTERS – SMALL &amp; LARGE <span style="font-weight:400;font-size:11px">(small serves 10–15, large serves 20–30)</span></h3>
      <div class="menu-row"><span>Fresh Fruit Platter</span><span class="dots"></span><span class="price">$35 / $60</span></div>
      <div class="menu-row"><span>Vegetable Crudités &amp; Ranch</span><span class="dots"></span><span class="price">$30 / $55</span></div>
      <div class="menu-row"><span>Cheese &amp; Cracker Board</span><span class="dots"></span><span class="price">$40 / $70</span></div>
      <h3 class="sec-title">DESSERT OPTIONS <span style="font-weight:400;font-size:11px">(price is by the dozen)</span></h3>
      <div class="menu-row"><span>Chocolate Brownies</span><span class="dots"></span><span class="price">$12</span></div>
      <div class="menu-row"><span>Fresh Baked Cookies</span><span class="dots"></span><span class="price">$10</span></div>
      <div class="menu-row"><span>Mini Cheesecakes</span><span class="dots"></span><span class="price">$20</span></div>
      <h3 class="sec-title">BEVERAGE OPTIONS</h3>
      <ul class="list">
        <li><strong>Full Bar:</strong> guests order and pay for their own drinks</li>
        <li><strong>Host Bar:</strong> all drinks added to the final bill</li>
        <li><strong>Drink Tickets:</strong> host buys a set number of tickets</li>
        <li><strong>Soft Drinks &amp; Coffee:</strong> $2.50 per guest</li>
      </ul>
      <div class="photo-strip">
        <div class="photo ms-1" role="img" aria-label="Photo of a salad bar spread"></div>
        <div class="photo ms-2" role="img" aria-label="Photo of the private dining room set for guests"></div>
        <div class="photo ms-3" role="img" aria-label="Photo of a fresh fruit platter"></div>
      </div>
    </article>
  </section>

  <!-- Inside spread 2: lunch + dinner options -->
  <section class="spread">
    <article class="page inside">
      <h2 class="page-head">LUNCH OPTIONS</h2>
      <p class="head-note">(an option must be chosen for groups of 15 or more, served before 3pm)</p>
      <h3 class="option-title">OPTION A – $16.45/PERSON</h3>
      <p class="body-text">Pick two lunch entrées – served family style:</p>
      <ul class="list">
        <li>Sandwiches: turkey club, BLT or smoked pulled pork</li>
        <li>Salads: grilled chicken Caesar or house garden</li>
        <li>Served with house-made chips and a soft drink</li>
      </ul>
      <h3 class="option-title">OPTION B – $15/PERSON</h3>
      <p class="body-text">Guests order from a select lunch menu of burgers, wraps and salads on the day of your event.</p>
      <h3 class="option-title">OPTION C – $15/PERSON BUFFET OPTION</h3>
      <ul class="list">
        <li>Rotisserie chicken salad bar with fresh toppings</li>
        <li>Food ready upon arrival, or at a set time of your choice</li>
      </ul>
      <div class="lunch-photos">
        <div class="interior" role="img" aria-label="Photo of the restaurant dining room interior"></div>
        <div class="food-stack">
          <div class="food-item"><div class="photo lp-1" role="img" aria-label="Photo of a chicken salad bar"></div><p class="food-caption">Rotisserie Chicken Salad Bar</p></div>
          <div class="food-item"><div class="photo lp-2" role="img" aria-label="Photo of house-made potato chips"></div><p class="food-caption">House-made Potato Chips</p></div>
          <div class="food-item"><div class="photo lp-3" role="img" aria-label="Photo of a fresh fruit platter"></div><p class="food-caption">Fresh Fruit Platter</p></div>
        </div>
      </div>
    </article>

    <article class="page inside">
      <h2 class="page-head">DINNER OPTIONS</h2>
      <p class="head-note">(an option must be chosen for groups of 15 or more, served after 3pm)</p>
      <p class="body-text" style="margin-bottom:6px">All dinner options include a house salad, warm rolls, soft drinks and coffee, served family style to every table.</p>
      <div class="dining-photo" role="img" aria-label="Photo of the private dining room with set tables"></div>
      <h3 class="option-title">OPTION A – $20/PERSON</h3>
      <p class="body-text">Choose two entrées:</p>
      <ul class="list">
        <li>Wood-fired half chicken</li>
        <li>BBQ baby back ribs</li>
        <li>Grilled salmon with lemon</li>
        <li>Pasta primavera</li>
      </ul>
      <div style="clear:both"></div>
      <h3 class="option-title">OPTION B – $27/PERSON</h3>
      <p class="body-text">Choose three entrées, served with roasted potatoes and seasonal vegetables:</p>
      <ul class="list">
        <li>Wood-fired sirloin steak</li>
        <li>Full rack of BBQ ribs</li>
        <li>Grilled salmon or herb chicken</li>
      </ul>
      <div class="dinner-photo" role="img" aria-label="Photo of glazed grilled chicken wings with greens"></div>
    </article>
  </section>

</main>
</body>
</html>
```